Local Flower Farm Needs Business Card Design

I need business cards designed for a flower farm based in Eudora, Kansas.
Business Info:
We are a local cut flower farm located in Eudora, Kansas, founded by Darla Hoffstrom. What started as a passion for agriculture and search for more joy in daily life has blossomed into a small business dedicated to providing the community with beautiful, fresh, and sustainable flowers. We specialize in local, seasonal blooms, ensuring that every petal reflects the care and dedication we pour into our craft. Our mission is to deliver the highest quality flowers directly to our customers through local farmers markets and to florists who share our commitment to sustainability. Join us in celebrating the beauty of nature, one bloom at a time!
Contact Details:
Darla Hoffstrom
Owner
Phone 913-555-0147
Facebook: Lorabelle Quinn Blossoms
Instagram: @LorabelleQuinnBlossoms
Website: LorabelleQuinnBlossoms.example
Target Market(s)
Wholesale to Florists and Direct to Consumer via Farmers Market
Industry/Entity Type
Florist, Farm
Contact Information for Business Card
Name, Contact Info, Logo
Look and feel

```html
<!DOCTYPE html>
<html lang="en">
<head>
<meta charset="utf-8">
<title>Lorabelle Quinn Blossoms — Business Card</title>
<link rel="stylesheet" href="https://fonts.googleapis.com/css2?family=Noto+Serif:wght@700&family=Tinos:wght@400&display=swap">
<style>
  :root {
    --page: #e9eaea;
    --ink: #0d2a2f;
    --card-back: #0b2a30;
    --card-back-mark: #174148;
    --card-front: #ffffff;
    --text: #111a1c;
  }
  * { margin: 0; padding: 0; box-sizing: border-box; }
  html, body { width: 1200px; height: 901px; overflow: hidden; }
  body {
    background: var(--page);
    font-family: "Tinos", "Times New Roman", serif;
    color: var(--text);
  }
  .stage {
    position: relative;
    width: 1200px;
    height: 901px;
  }
  .card {
    position: absolute;
    left: 290px;
    width: 620px;
    height: 354px;
    border-radius: 22px;
    overflow: hidden;
    box-shadow: 0 6px 18px rgba(0,0,0,0.12);
  }
  .card--back { top: 60px; background: var(--card-back); }
  .card--front { top: 446px; background: var(--card-front); }

  .back-mark {
    position: absolute;
    left: 50%; top: 50%;
    width: 220px; height: 220px;
    transform: translate(-50%, -50%);
    border: 1.5px solid var(--card-back-mark);
    border-radius: 50%;
    display: flex; align-items: center; justify-content: center;
    text-align: center;
  }
  .back-mark__name {
    font-family: "Tinos", serif;
    font-weight: 400;
    font-size: 22px;
    line-height: 1.3;
    letter-spacing: 3px;
    text-transform: uppercase;
    color: var(--card-back-mark);
  }

  .identity {
    position: absolute;
    left: 0; top: 34px;
    padding-left: 30px;
  }
  .identity__bar {
    position: absolute;
    left: 0; top: 4px;
    width: 8px; height: 42px;
    background: var(--ink);
  }
  .identity__name {
    font-family: "Noto Serif", Georgia, serif;
    font-weight: 700;
    font-size: 27px;
    color: var(--ink);
    line-height: 1.1;
  }
  .identity__role {
    font-size: 14px;
    color: var(--text);
    margin-top: 2px;
  }

  .contacts {
    position: absolute;
    left: 30px; bottom: 34px;
    list-style: none;
  }
  .contacts__item {
    display: flex; align-items: center;
    font-size: 17px;
    line-height: 1;
    margin-top: 11px;
  }
  .contacts__icon {
    width: 15px; height: 15px;
    margin-right: 10px;
    flex: none;
  }
  .contacts__square {
    width: 13px; height: 13px;
    margin: 0 11px 0 1px;
    background: var(--ink);
    border-radius: 2px;
    flex: none;
  }

  .front-mark {
    position: absolute;
    right: 40px; top: 50%;
    width: 252px; height: 252px;
    transform: translateY(-50%);
    border: 1.5px solid var(--ink);
    border-radius: 50%;
    display: flex; align-items: center; justify-content: center;
    text-align: center;
  }
  .front-mark__name {
    font-family: "Tinos", serif;
    font-weight: 400;
    font-size: 25px;
    line-height: 1.3;
    letter-spacing: 3px;
    text-transform: uppercase;
    color: var(--ink);
  }
</style>
</head>
<body>
<main class="stage">

  <section class="card card--back" aria-label="Card back">
    <div class="back-mark">
      <p class="back-mark__name">Lorabelle<br>Quinn<br>Blossoms</p>
    </div>
  </section>

  <section class="card card--front" aria-label="Card front">
    <header class="identity">
      <span class="identity__bar"></span>
      <h1 class="identity__name">Darla Hoffstrom</h1>
      <p class="identity__role">Owner</p>
    </header>

    <ul class="contacts">
      <li class="contacts__item">
        <svg class="contacts__icon" viewBox="0 0 24 24" aria-hidden="true">
          <path fill="#0d2a2f" d="M6.6 10.8a15.1 15.1 0 0 0 6.6 6.6l2.2-2.2a1 1 0 0 1 1-.25 11.4 11.4 0 0 0 3.6.57 1 1 0 0 1 1 1V20a1 1 0 0 1-1 1A17 17 0 0 1 3 4a1 1 0 0 1 1-1h3.5a1 1 0 0 1 1 1c0 1.25.2 2.45.57 3.57a1 1 0 0 1-.25 1z"/>
        </svg>
        913-555-0147
      </li>
      <li class="contacts__item">
        <svg class="contacts__icon" viewBox="0 0 24 24" aria-hidden="true">
          <circle cx="12" cy="12" r="10" fill="none" stroke="#0d2a2f" stroke-width="2"/>
          <ellipse cx="12" cy="12" rx="4.5" ry="10" fill="none" stroke="#0d2a2f" stroke-width="1.6"/>
          <line x1="2" y1="12" x2="22" y2="12" stroke="#0d2a2f" stroke-width="1.6"/>
        </svg>
        LorabelleQuinnBlossoms.example
      </li>
      <li class="contacts__item">
        <span class="contacts__square"></span>
        Lorabelle Quinn Blossoms
      </li>
      <li class="contacts__item">
        <span class="contacts__square"></span>
        @LorabelleQuinnBlossoms
      </li>
    </ul>

    <div class="front-mark">
      <p class="front-mark__name">Lorabelle<br>Quinn<br>Blossoms</p>
    </div>
  </section>

</main>
</body>
</html>
```